Wix Website for Bookkeeper - make me stand out! :)

I would like Wix website to promote my bookkeeping business. The pages that I need to create are: Home, About, Services, For Accountants, Contact Us &
Landing Page (offering a 5 part email series called "7 Lessons Every Shop Keeper NEEDS to learn")

I would like to offer the ability for potential clients to book a 'Complimentary Ledger Review'.

I had a logo designed on Taskloft which is supposed to look like a building/calculator - I like the concept but I'm happy to have it redsigned/new colours if you don't think it works for whatever reason.

I tried to create a website myself using a template but I'm not happy with it at all. It just looks too much like a boring bookkeeping site! Haha! https://www.plumridgeledgers.com.au/
Updates

Hi All - I've seen a number of good designs but I still have an open mind. If you have not yet submitted, please do and I will give you fast feedback. Thanks, Trevor

Target Market(s)

Small Business Owners

Coding

Coded - Design and coding required

Number of Pages Required

5+ page

Font styles to use
Sans Serif

Requirements
Must have
• Mobile optimised
Nice to have
• Less is more :)

```html
<!DOCTYPE html>
<html lang="en">
<head>
<meta charset="utf-8">
<title>Services – Plumridge Ledgers</title>
<link rel="stylesheet" href="https://fonts.googleapis.com/css2?family=Lato:ital,wght@0,400;0,700;0,900;1,700&display=swap">
<style>
  :root {
    --blue: #0a6ff0;
    --ink: #3a3a3a;
    --text: #444;
    --rule: #cfcfcf;
    --card-border: #d6d6d6;
    --band: #d8d0cb;
    --footer: #1c1c1c;
    --footer-text: #f2f2f2;
    --muted: #8d8d8d;
  }
  * { box-sizing: border-box; margin: 0; padding: 0; }
  html, body { width: 932px; height: 1200px; overflow: hidden; }
  body { font-family: "Lato", Arial, sans-serif; color: var(--text); background: #fff; position: relative; }

  .site-header { position: absolute; left: 0; top: 0; width: 932px; height: 95px; background: #fff; box-shadow: 0 2px 6px rgba(0,0,0,.18); z-index: 2; }
  .brand { position: absolute; left: 58px; top: 26px; display: flex; align-items: center; gap: 8px; }
  .brand-mark { width: 38px; height: 44px; background: var(--blue); }
  .brand-name { font-weight: 900; font-size: 22px; line-height: 1.05; color: var(--blue); letter-spacing: .5px; }
  .main-nav { position: absolute; right: 56px; top: 42px; display: flex; gap: 28px; }
  .main-nav a { font-size: 12px; font-weight: 700; color: var(--ink); text-decoration: none; }
  .main-nav a.is-active { color: var(--blue); }

  .page-title { position: absolute; left: 58px; top: 128px; font-size: 25px; font-weight: 900; color: var(--ink); }
  .title-rule { position: absolute; left: 58px; top: 171px; width: 816px; height: 1px; background: var(--rule); }
  .section-heading { position: absolute; left: 0; width: 932px; top: 204px; text-align: center; font-size: 22px; font-weight: 900; color: var(--blue); }

  .package { position: absolute; top: 255px; width: 256px; height: 401px; border: 1px solid var(--card-border); background: #fff; }
  .package h3 { position: absolute; left: 16px; top: 22px; font-size: 17px; font-weight: 900; color: var(--ink); }
  .package ul { position: absolute; left: 16px; top: 55px; list-style: none; }
  .package li { height: 28px; display: flex; align-items: center; font-size: 11.3px; color: var(--text); letter-spacing: .2px; }
  .package li svg { width: 11px; height: 9px; margin-right: 15px; flex: none; }
  .btn-enquire { position: absolute; left: 61px; top: 348px; width: 134px; height: 29px; background: var(--blue); color: #fff; font-size: 13.5px; font-weight: 900; display: flex; align-items: center; justify-content: center; }

  .system-band { position: absolute; left: 0; top: 708px; width: 932px; height: 304px; background: var(--band); overflow: hidden; }
  .system-photo { position: absolute; right: 0; top: 0; width: 460px; height: 304px;
    background: linear-gradient(90deg, var(--band) 0%, #e6e2dc 30%, #eef0ec 55%, #c9d7c0 75%, #5d6b4a 100%); }
  .system-band h2 { position: absolute; left: 57px; top: 48px; font-size: 25px; font-weight: 900; color: var(--ink); position: absolute; }
  .system-band p { position: absolute; left: 57px; top: 88px; width: 455px; font-size: 11.5px; line-height: 21.5px; color: var(--text); }
  .system-band .agent-note { top: 205px; width: 470px; font-size: 14px; line-height: 21.5px; font-weight: 700; font-style: italic; color: var(--blue); }

  .site-footer { position: absolute; left: 0; top: 1012px; width: 932px; height: 188px; background: var(--footer); color: var(--footer-text); }
  .footer-brand { position: absolute; left: 58px; top: 53px; display: flex; align-items: center; gap: 6px; }
  .footer-brand .brand-mark { width: 28px; height: 34px; background: var(--muted); }
  .footer-brand .brand-name { font-size: 17px; color: var(--muted); }
  .copyright { position: absolute; left: 58px; top: 106px; font-size: 10px; line-height: 17.5px; }
  .footer-col { position: absolute; top: 37px; }
  .footer-col h4 { font-size: 14px; font-weight: 700; margin-bottom: 8px; }
  .footer-col a, .footer-col span { display: block; font-size: 11px; color: var(--footer-text); text-decoration: none; line-height: 22px; }
  .contact-line { display: flex; align-items: center; gap: 14px; }
  .contact-line svg { width: 11px; height: 11px; flex: none; }
  .social { display: flex; gap: 18px; margin-top: 4px; }
  .social span { width: 22px; height: 22px; border-radius: 50%; background: var(--footer-text); }
</style>
</head>
<body>
  <header class="site-header">
    <div class="brand">
      <div class="brand-mark"></div>
      <div class="brand-name">PLUMRIDGE<br>LEDGERS</div>
    </div>
    <nav class="main-nav">
      <a href="#">HOME</a>
      <a href="#">ABOUT</a>
      <a href="#" class="is-active">SERVICES</a>
      <a href="#">FOR ACCOUNTANTS</a>
      <a href="#">CONTACT US</a>
    </nav>
  </header>

  <h1 class="page-title">SERVICES</h1>
  <div class="title-rule"></div>
  <h2 class="section-heading">OUR PACKAGES</h2>

  <svg width="0" height="0" style="position:absolute">
    <symbol id="tick" viewBox="0 0 11 9"><path d="M1 4.6 4 7.5 10 1.3" fill="none" stroke="#0a6ff0" stroke-width="2.4"/></symbol>
  </svg>

  <section class="package" style="left:58px">
    <h3>STARTER</h3>
    <ul>
      <li><svg><use href="#tick"/></svg>Duis ultrices erat</li>
      <li><svg><use href="#tick"/></svg>Hendrerit accumsan</li>
      <li><svg><use href="#tick"/></svg>Proin eget eros at erat egestas</li>
      <li><svg><use href="#tick"/></svg>Faucibus in vitae lacus</li>
      <li><svg><use href="#tick"/></svg>Donec eu tortor</li>
      <li><svg><use href="#tick"/></svg>Felis imperdiet aliquet</li>
      <li><svg><use href="#tick"/></svg>Vel at elit</li>
      <li><svg><use href="#tick"/></svg>Nunc tempus id dui sit</li>
      <li><svg><use href="#tick"/></svg>Amet tincidunt</li>
      <li><svg><use href="#tick"/></svg>Sed eget posuere justo</li>
    </ul>
    <a class="btn-enquire">ENQUIRE</a>
  </section>

  <section class="package" style="left:338px">
    <h3>MEDIUM</h3>
    <ul>
      <li><svg><use href="#tick"/></svg>Duis ultrices erat</li>
      <li><svg><use href="#tick"/></svg>Hendrerit accumsan</li>
      <li><svg><use href="#tick"/></svg>Proin eget eros at erat egestas</li>
      <li><svg><use href="#tick"/></svg>Faucibus in vitae lacus</li>
      <li><svg><use href="#tick"/></svg>Donec eu tortor</li>
      <li><svg><use href="#tick"/></svg>Felis imperdiet aliquet</li>
      <li><svg><use href="#tick"/></svg>Vel at elit</li>
      <li><svg><use href="#tick"/></svg>Nunc tempus id dui sit</li>
      <li><svg><use href="#tick"/></svg>Amet tincidunt</li>
      <li><svg><use href="#tick"/></svg>Sed eget posuere justo</li>
    </ul>
    <a class="btn-enquire">ENQUIRE</a>
  </section>

  <section class="package" style="left:617px">
    <h3>LARGE</h3>
    <ul>
      <li><svg><use href="#tick"/></svg>Duis ultrices erat</li>
      <li><svg><use href="#tick"/></svg>Hendrerit accumsan</li>
      <li><svg><use href="#tick"/></svg>Proin eget eros at erat egestas</li>
      <li><svg><use href="#tick"/></svg>Faucibus in vitae lacus</li>
      <li><svg><use href="#tick"/></svg>Donec eu tortor</li>
      <li><svg><use href="#tick"/></svg>Felis imperdiet aliquet</li>
      <li><svg><use href="#tick"/></svg>Vel at elit</li>
      <li><svg><use href="#tick"/></svg>Nunc tempus id dui sit</li>
      <li><svg><use href="#tick"/></svg>Amet tincidunt</li>
      <li><svg><use href="#tick"/></svg>Sed eget posuere justo</li>
    </ul>
    <a class="btn-enquire">ENQUIRE</a>
  </section>

  <section class="system-band">
    <div class="system-photo" role="img" aria-label="Photo of a bookkeeper working at a desk with a calculator, paperwork and computer monitors"></div>
    <h2>CLEARLINE BOOKKEEPING SYSTEM</h2>
    <p>We are proud to use the Clearline Bookkeeping System with all of our clients. CBS is kept constantly updated as changes occur in legislation or with software changes and is endorsed by the National Bookkeepers' Alliance - Australia's premier professional body for bookkeepers. As we are an accredited licensee you can relax knowing that the finances of your business are in good hands!</p>
    <p class="agent-note">We work with Registered Tax Agent Keystone Lodgement Pty Ltd (Tax Agent # 8402615) to facilitate the lodgement of our clients activity statements.</p>
  </section>

  <footer class="site-footer">
    <div class="footer-brand">
      <div class="brand-mark"></div>
      <div class="brand-name">PLUMRIDGE<br>LEDGERS</div>
    </div>
    <div class="copyright">COPYRIGHT © 2020 PLUMRIDGE LEDGERS (WA) PTY LTD<br>ALL RIGHT RESERVED</div>

    <div class="footer-col" style="left:337px">
      <h4>SITE MAP</h4>
      <a href="#">Home</a>
      <a href="#">About</a>
      <a href="#">Services</a>
      <a href="#">For Accountants</a>
      <a href="#">Contact Us</a>
    </div>

    <div class="footer-col" style="left:499px">
      <h4>CONTACT INFO</h4>
      <span>Larkmoor, Western Australia</span>
      <span class="contact-line" style="margin-top:5px"><svg viewBox="0 0 12 12"><path d="M2.5 1h2l1 3-1.3 1a7 7 0 0 0 2.8 2.8l1-1.3 3 1v2c0 .8-.6 1.5-1.5 1.5C5 11 1 7 1 2.5 1 1.6 1.7 1 2.5 1z" fill="#f2f2f2"/></svg>0491 570 110</span>
      <span class="contact-line"><svg viewBox="0 0 12 12"><path d="M0 2.5h12v7.5H0z" fill="#f2f2f2"/><path d="M0 2.5l6 4.5 6-4.5" fill="none" stroke="#1c1c1c" stroke-width="1"/></svg>hello@plumridgeledgers.com.au</span>
    </div>

    <div class="footer-col" style="left:717px">
      <h4>FOLLOW US</h4>
      <div class="social"><span></span><span></span></div>
    </div>
  </footer>
</body>
</html>
```